Plumbing and heating business card design

i need a new business card for the company i work for called Dr. Brightpipe. It is a plumbing and heating company that has been operating for over 30 years. We are not like these big plumbing companies that have ways to charge the customer as much as possible. Our company does only what is necessary and what is needed to do the job right the first time without the high cost. we are a neighborhood business which kind of explains why we don't charge customers through the roof. I would like to see a design with a nice background anything but just plain white. maybe like a light blue at the top of the design. on the back of the card i would like it to say " T. Vandermeer's Dr. Brightpipe". maybe add some color to the lettering on the front of the card for example blue font for plumbing and red font for heating. raised print. im sure Cardolux designers will make it look good. The final design should help spread a good word about our company and help grow business.

Industry/Entity Type

Business

Contact Information for Business Card

Dr. Brightpipe, Plumbing & heating, Gordon Tasker, Northeast District Operations manager, 4827 Birchwell st., Office:(555)-284-1937, doctorbrightpipe@mailverra.net

Requirements
Must have
• raised print finish and a nice sturdy feel.

```html
<!DOCTYPE html>
<html lang="en">
<head>
<meta charset="utf-8">
<title>Dr. Brightpipe Business Cards</title>
<link href="https://fonts.googleapis.com/css2?family=Montserrat:wght@400;500;700;800&display=swap" rel="stylesheet">
<style>
  :root {
    --bg: #e9e6e2;
    --card: #000000;
    --white: #ffffff;
    --silver: #cfcfcf;
    --blue: #2e56a6;
    --teal: #2f5f7a;
    --red: #a11c22;
  }
  html, body {
    margin: 0;
    width: 1200px;
    height: 1000px;
    overflow: hidden;
    background: var(--bg);
    font-family: "Montserrat", Arial, sans-serif;
  }
  .stage { position: relative; width: 1200px; height: 1000px; }

  .card {
    position: absolute;
    background: var(--card);
    box-shadow: 0 6px 16px rgba(0,0,0,.25);
    overflow: hidden;
  }

  .brand-dot {
    display: block;
    border-radius: 50%;
    background: var(--silver);
  }

  /* Back card */
  .card-back { left: 115px; top: 95px; width: 640px; height: 360px; }
  .back-lockup {
    position: absolute; left: 0; right: 0; top: 40px;
    display: flex; flex-direction: column; align-items: center;
    color: var(--silver);
    text-align: center;
  }
  .back-lockup .brand-dot { width: 64px; height: 64px; margin-bottom: 12px; }
  .owner-line { font-size: 21px; font-weight: 500; line-height: 1.2; }
  .brand-line { font-size: 44px; font-weight: 800; line-height: 1.1; }
  .tagline-line { font-size: 19px; font-weight: 500; line-height: 1.25; margin-top: 2px; }
  .back-phone {
    position: absolute;
    color: var(--white); font-size: 18px; font-weight: 500;
    white-space: nowrap;
  }
  .phone-bucks { right: 36px; bottom: 86px; }
  .phone-phila { left: 36px; bottom: 34px; }

  /* Front card */
  .card-front { left: 413px; top: 527px; width: 617px; height: 362px; }
  .front-lockup {
    position: absolute; left: 34px; top: 30px;
    display: flex; align-items: center; gap: 14px;
  }
  .front-lockup .brand-dot { width: 56px; height: 56px; background: var(--teal); }
  .front-name { color: var(--silver); font-weight: 800; font-size: 33px; line-height: 1; }
  .front-tagline { font-size: 15px; font-weight: 700; margin-top: 4px; }
  .tag-plumbing { color: var(--blue); }
  .tag-and { color: var(--silver); }
  .tag-hvac { color: var(--red); }
  .person { position: absolute; left: 40px; top: 155px; }
  .person-name { color: var(--blue); font-size: 27px; font-weight: 500; }
  .person-role { color: var(--white); font-size: 13px; margin-top: 2px; }
  .contacts { position: absolute; left: 40px; top: 238px; list-style: none; margin: 0; padding: 0; }
  .contacts li {
    display: flex; align-items: center; gap: 14px;
    color: var(--white); font-size: 14px; height: 31px;
    white-space: nowrap;
  }
  .contacts svg { width: 26px; height: 26px; flex: none; }
  .swoosh { position: absolute; right: 0; top: 0; width: 290px; height: 362px; }

  /* Standalone lockup */
  .lockup-standalone {
    position: absolute; left: 835px; top: 62px; width: 320px;
    display: flex; flex-direction: column; align-items: center;
    color: var(--white);
    text-align: center;
  }
  .lockup-standalone .brand-dot { background: var(--white); width: 70px; height: 70px; margin-bottom: 14px; }
  .lockup-standalone .owner-line { font-size: 21px; font-weight: 700; }
  .lockup-standalone .brand-line { font-size: 40px; }
  .lockup-standalone .tagline-line { font-size: 18px; font-weight: 700; }
</style>
</head>
<body>
<main class="stage">

  <section class="card card-back" aria-label="Card back">
    <div class="back-lockup">
      <span class="brand-dot"></span>
      <div class="owner-line">T. Vandermeer's</div>
      <div class="brand-line">Dr. Brightpipe</div>
      <div class="tagline-line">Plumping and HVAC</div>
    </div>
    <div class="back-phone phone-bucks">Bucks (555)-613-0482</div>
    <div class="back-phone phone-phila">Phila (555)-284-1937</div>
  </section>

  <section class="card card-front" aria-label="Card front">
    <div class="front-lockup">
      <span class="brand-dot"></span>
      <div>
        <div class="front-name">Dr. Brightpipe</div>
        <div class="front-tagline"><span class="tag-plumbing">Plumping</span> <span class="tag-and">and</span> <span class="tag-hvac">HVAC</span></div>
      </div>
    </div>

    <div class="person">
      <div class="person-name">Gordon Tasker</div>
      <div class="person-role">Northeast District Operations Manager</div>
    </div>

    <ul class="contacts">
      <li>
        <svg viewBox="0 0 24 24"><path d="M12 2a7 7 0 0 0-7 7c0 5 7 13 7 13s7-8 7-13a7 7 0 0 0-7-7z" fill="#2e56a6"/><circle cx="12" cy="9" r="3" fill="#a11c22"/></svg>
        4827 Birchwell st.
      </li>
      <li>
        <svg viewBox="0 0 24 24"><circle cx="12" cy="12" r="11" fill="#2e56a6"/><path d="M8 6l2 3-1.5 1.5a8 8 0 0 0 5 5L15 14l3 2-1 2.5c-5 0-10-5-10-10z" fill="#a11c22"/></svg>
        (555)-284-1937
      </li>
      <li>
        <svg viewBox="0 0 24 24"><rect x="2" y="4" width="20" height="16" rx="2" fill="#2e56a6"/><path d="M2 6l10 7 10-7" fill="none" stroke="#a11c22" stroke-width="2"/></svg>
        doctorbrightpipe@mailverra.net
      </li>
    </ul>

    <svg class="swoosh" viewBox="0 0 300 362" preserveAspectRatio="none" aria-hidden="true">
      <defs>
        <linearGradient id="silverBand" x1="0" y1="0" x2="1" y2="1">
          <stop offset="0" stop-color="#f2f2f2"/>
          <stop offset="1" stop-color="#555555"/>
        </linearGradient>
      </defs>
      <path d="M0 362 C10 170 130 40 300 0 L300 362 Z" fill="var(--teal)"/>
      <path d="M78 362 C85 200 180 70 300 25 L300 362 Z" fill="url(#silverBand)"/>
      <path d="M168 362 C150 230 200 110 300 55 L300 362 Z" fill="var(--red)"/>
    </svg>
  </section>

  <div class="lockup-standalone" aria-label="Brand lockup">
    <span class="brand-dot"></span>
    <div class="owner-line">T. Vandermeer's</div>
    <div class="brand-line">Dr. Brightpipe</div>
    <div class="tagline-line">Plumping and HVAC</div>
  </div>

</main>
</body>
</html>
```